Redesign of Smart Watch Gift Voucher-SEE ATTACHED CURRENT DESIGN

I need to redesign my existing design using all same content and elements.

MY ENVISION: I invision more of a professional advertisement type of flyer/voucher. Imagine how Corvel.com would create a professionally looking flyer promoting the lumo or veno.

you can get many ideas about professional design by looking at some of corvels flyer designs :
https://www.findora-example.net/search?q=lumo+advertisment&mode=img&ref=a83kd02mzq7

stock photos are attached, you do not have to use them all, you can use some or none i am open to your designs using your own images if you want...just make sure the smartwatch looks black

DO NOT LEAVE ANY CONTENT OR ELEMENTS OUT ON MOCK UP PLEASE

SEE ATTACHED CURRENT DESIGN

I need to redesign my existing design using all same content and elements. DO NOT LEAVE ANY CONTENT OR ELEMENTS OUT ON MOCK UP PLEASE

Target Market(s)

B2B-you can get many ideas about professional design by looking at some of corvels flyer designs :

Industry/Entity Type

Marketing

Requirements
Must have
• I need to redesign my existing design using all same content and elements. DO NOT LEAVE ANY CONTENT OR ELEMENTS OUT ON MOCK UP PLEASE

Nice to have

Should not have

```html
<!DOCTYPE html>
<html lang="en">
<head>
<meta charset="utf-8">
<title>Smart Fitness Watch Voucher</title>
<link rel="stylesheet" href="https://fonts.googleapis.com/css2?family=Bebas+Neue&family=Montserrat:wght@500;600;700&family=Open+Sans:wght@400;600&display=swap">
<style>
  :root {
    --red: #d21f26;
    --deep-red: #a8141b;
    --title-red: #b5121b;
    --charcoal: #262626;
    --ink: #1d1d1d;
    --paper: #ffffff;
    --stage: #eceeef;
  }
  * { box-sizing: border-box; margin: 0; padding: 0; }
  html, body { width: 869px; height: 1200px; overflow: hidden; background: var(--paper); }
  .voucher {
    position: relative; width: 869px; height: 1200px; overflow: hidden;
    background: var(--paper); color: var(--ink);
    font-family: "Open Sans", Arial, sans-serif;
  }
  .layer { position: absolute; left: 0; top: 0; }
  .headline {
    position: absolute; left: 36px; top: 52px;
    font-family: "Bebas Neue", "Oswald", sans-serif;
    font-size: 58px; line-height: 1; letter-spacing: 0.2px;
    color: var(--title-red);
  }
  .subhead {
    position: absolute; left: 36px; top: 151px;
    font-family: "Montserrat", Arial, sans-serif; font-weight: 600;
    font-size: 19px; color: var(--paper); letter-spacing: 0.1px;
  }
  .intro {
    position: absolute; left: 59px; top: 332px; width: 372px;
    font-size: 13.2px; line-height: 18.2px; text-align: justify;
  }
  .features {
    position: absolute; left: 59px; top: 500px; width: 420px;
    display: grid; grid-template-columns: 225px 195px; row-gap: 4.6px;
    list-style: none; font-size: 13.2px; line-height: 18px;
  }
  .features li { position: relative; padding-left: 18px; }
  .features li::before {
    content: ""; position: absolute; left: 0; top: 4px; width: 9px; height: 9px;
    border: 1.4px solid var(--red);
  }
  .features li::after {
    content: ""; position: absolute; left: 3px; top: 3px; width: 4px; height: 8px;
    border-right: 2px solid var(--red); border-bottom: 2px solid var(--red);
    transform: rotate(40deg);
  }
  .section-title {
    position: absolute; left: 59px; top: 661px;
    font-family: "Montserrat", Arial, sans-serif; font-weight: 700;
    font-size: 19px; color: var(--red);
  }
  .how-text {
    position: absolute; left: 59px; top: 698px; width: 370px;
    font-size: 13.2px; line-height: 18.3px; text-align: justify;
  }
  .testimonial {
    position: absolute; left: 59px; top: 866px; width: 400px; color: var(--paper);
  }
  .testimonial h3 {
    font-family: "Montserrat", Arial, sans-serif; font-weight: 700; font-size: 20px;
    margin-bottom: 6px;
  }
  .testimonial p { font-size: 14px; line-height: 19px; }
  .testimonial .author {
    text-align: right; font-family: "Montserrat", Arial, sans-serif;
    font-weight: 700; font-size: 14px; margin-top: 2px;
  }
  .redeem { position: absolute; left: 57px; top: 1001px; width: 380px; }
  .redeem p { font-size: 13.6px; line-height: 17px; }
  .redeem .site {
    font-family: "Montserrat", Arial, sans-serif; font-weight: 700;
    font-size: 18px; margin-top: 2px;
  }
  .redeem .terms { font-size: 11.4px; margin-top: 4px; }
  .codes {
    position: absolute; left: 59px; top: 1110px;
    font-family: "Montserrat", Arial, sans-serif; font-weight: 700;
    font-size: 20px; line-height: 29px;
  }
  .codes span { color: var(--red); }
</style>
</head>
<body>
<main class="voucher">

  <svg class="layer" width="869" height="330" viewBox="0 0 869 330" aria-hidden="true">
    <defs>
      <linearGradient id="redBand" x1="0" x2="1">
        <stop offset="0" stop-color="var(--deep-red)"/>
        <stop offset="1" stop-color="var(--red)"/>
      </linearGradient>
    </defs>
    <rect x="0" y="0" width="869" height="38" fill="url(#redBand)"/>
    <polygon points="0,38 720,38 650,118 0,118" fill="var(--paper)"/>
    <polygon points="700,38 869,38 869,330 740,330 700,118 770,38" fill="var(--red)"/>
    <polygon points="0,135 800,135 745,190 0,190" fill="var(--charcoal)"/>
    <polygon points="38,190 745,190 690,260 300,220 38,240" fill="var(--red)"/>
    <polygon points="0,245 38,240 300,220 690,260 560,300 330,312 0,290" fill="var(--charcoal)"/>
    <polygon points="720,190 800,135 869,135 869,200 790,310" fill="var(--red)" opacity="0.85"/>
  </svg>

  <h1 class="headline">ENJOY YOUR BRAND NEW SMARTWATCH</h1>
  <h2 class="subhead">TAKE CONTROL OF YOUR LIFE WITH YOUR NEW SMART FITNESS WATCH</h2>

  <svg class="layer" style="left:447px;top:210px" width="400" height="480" viewBox="0 0 400 480" role="img" aria-label="Product photo of the black smart fitness watch with a square touchscreen and black strap">
    <defs>
      <linearGradient id="watchTone" x1="0" y1="0" x2="1" y2="1">
        <stop offset="0" stop-color="#4a4a4e"/>
        <stop offset="1" stop-color="#111113"/>
      </linearGradient>
      <radialGradient id="watchShadow">
        <stop offset="0" stop-color="#555" stop-opacity="0.7"/>
        <stop offset="1" stop-color="#555" stop-opacity="0"/>
      </radialGradient>
    </defs>
    <rect x="150" y="0" width="180" height="470" rx="40" fill="#1a1a1a"/>
    <rect x="20" y="40" width="250" height="370" rx="36" fill="url(#watchTone)"/>
    <ellipse cx="208" cy="465" rx="120" ry="14" fill="url(#watchShadow)"/>
  </svg>

  <p class="intro">Congratulations, you have been rewarded with a Brand New Smart Fitness Watch shipped right to your door. Just pay shipping and handling. Your new Smart Fitness Watch has these features: sport mode, pedomoter, distance, calorie, heart rate, blood pressure, stopwatch, sleep monitoring, phone locator, reminders, remote camera, an alarm clock and much more!</p>

  <ul class="features">
    <li>Pedomoter</li><li>Distance Tracker</li>
    <li>Calorie Counter</li><li>Heart Rate Monitor</li>
    <li>Blood Pressure Monitor</li><li>Stopwatch</li>
    <li>Sleep Monitoring</li><li>Phone Locator</li>
    <li>Reminders Feature</li><li>Remote Camera</li>
    <li>Alarm Clock</li><li>Waterproof</li>
  </ul>

  <h3 class="section-title">HOW CAN WE DO THIS</h3>
  <p class="how-text">We have a couple retail partners that we team up with to "crowd purchase" huge shipping containers that hold 10's of thousands of electronic products at 80-90% off retail. We simply pass our savings on to you as we do not profit from our electronic products. You are basically able to "piggy back" on our partnerships and buying power to get an attractive electronic premium for a fraction of the retail cost.</p>

  <svg class="layer" style="top:684px" width="869" height="516" viewBox="0 684 869 516" role="img" aria-label="Photo of an athlete resting on stadium steps checking a smartwatch and phone, overlaid with blue fitness activity icons">
    <defs>
      <linearGradient id="runnerTone" x1="0" y1="0" x2="1" y2="1">
        <stop offset="0" stop-color="#dfe3e6"/>
        <stop offset="0.5" stop-color="#c9cdd0"/>
        <stop offset="1" stop-color="#e8d2c4"/>
      </linearGradient>
    </defs>
    <polygon points="545,694 869,755 869,1200 420,1200 398,1150 475,960 440,930 510,720" fill="url(#runnerTone)" stroke="var(--red)" stroke-width="5"/>
  </svg>

  <svg class="layer" style="top:852px" width="500" height="122" viewBox="0 0 500 122" aria-hidden="true">
    <defs>
      <linearGradient id="quoteBand" x1="0" x2="1">
        <stop offset="0" stop-color="var(--deep-red)"/>
        <stop offset="1" stop-color="var(--red)"/>
      </linearGradient>
    </defs>
    <path d="M0,0 H430 Q498,4 488,61 Q478,118 430,122 H0 Z" fill="url(#quoteBand)"/>
  </svg>

  <section class="testimonial">
    <h3>WHAT OTHERS SAY</h3>
    <p>"Are you sure this is not a Norvia Pulse Smartwatch in DISGUISE???? I love mine."</p>
    <p class="author">DYLAN K. ATLANTIC CITY, NJ</p>
  </section>

  <section class="redeem">
    <p>VIEW ALL THE DETAILS OF THIS SPECIAL OFFER AND REDEEM ONLINE AT:</p>
    <p class="site">www.perkvaultoffers.com</p>
    <p class="terms">*Terms and Conditions apply see website for details</p>
  </section>

  <div class="codes">
    <div>CERTIFICATE ID: <span>91772-89218</span></div>
    <div>EXPIRES: <span>10/03/2020</span></div>
  </div>

</main>
</body>
</html>
```